Promotional Flyer/Email Design - Cabling services for Broadcast and Audio Visual

We need a promotional flyer/email design to help launch our company, Velto Wire. We provide cabling services for Broadcast Television and Audio Visual systems. Recent projects include major television events such as the Harrowfield Racquet Open and Audio Visual/Entertainment systems for wealthy clients in their homes and on-board super yachts.

The flyer will be printed as single sided A5 and also be sent out in the body of a promotional email. It should feature the company logo along with a complementary colour scheme. It should have a clean finish with images that show the type of work we do (cabling and equipment installation) or the setting for these systems (tv studio, super yacht, cinema room, meeting room with projector etc.)

Services we offer are:

Broadcast/AV system design
On-site installation
Rack building
Pre-fabricated cable looms
Fibre optic installation

About the company:

Velto Wire provide cabling services for Broadcast Television and Audio Visual systems. With over 15 years experience working in these industries we can help with every aspect of design, project managment, installation and maintenance. Our projects range from fibre optic cabling at major sports events to installing and commisioning bespoke control systems on some of the worlds largest super yachts.

Contact details:

To get a quote or discuss your project contact us now
Telephone: TBC
Email: info@velto-wire.example
Website: www.velto-wire.example
Address: TBC

Other information:

The company is based in London, UK. Our projects often take place in other countries with work taking place accross Europe and beyond.

We have a London based workshop for rack building and cable pre-fabrication.

Our website is www.velto-wire.example

Images:

Images attached can be editted for use on the flyer or have ideas taken from them. Only the company logo is required to feature on the final design.

Target Market(s)

Business to business

Industry/Entity Type

It Company

Font styles to use
Sans Serif

Requirements
Must have
• Company logo
• List of services
• Contact details
Nice to have
• Image of cabling, home cinema room, super yacht, luxury home, outside broadcast truck, fibre optic equipment or cabling.

```html
<!DOCTYPE html>
<html lang="en">
<head>
<meta charset="utf-8">
<title>Velto Wire – Broadcast &amp; AV Cabling Flyer</title>
<link href="https://fonts.googleapis.com/css2?family=Montserrat:wght@400;500;600;700;800&display=swap" rel="stylesheet">
<style>
  :root{
    --page-bg:#e4e4e6;
    --charcoal:#2f2f32;
    --crimson:#dc1445;
    --sky-blue:#2f8ae6;
    --gold:#f2b50f;
    --quote-grey:#8e8e90;
    --ink:#2b2b2e;
    --muted:#7a7a7d;
    --white:#ffffff;
  }
  *{box-sizing:border-box;margin:0;padding:0}
  html,body{width:1200px;height:1200px;overflow:hidden}
  body{background:var(--page-bg);font-family:'Montserrat',sans-serif;position:relative}
  .flyer{position:absolute;left:200px;top:35px;width:800px;height:1130px;overflow:hidden;background:var(--charcoal);box-shadow:0 10px 30px rgba(0,0,0,.18)}
  .flyer-shapes{position:absolute;inset:0;width:800px;height:1130px}
  .abs{position:absolute}
  .event-badge{left:48px;top:92px;width:340px;color:var(--white)}
  .event-badge__lead{font-size:26px;font-weight:500;line-height:1.2}
  .event-badge__claim{font-size:26px;font-weight:800;line-height:1.15;margin-top:12px}
  .event-badge__note{font-size:11px;font-weight:400;margin-top:4px}
  .about{left:430px;top:488px;width:345px;color:var(--white);font-size:13px;line-height:1.45}
  .services{left:430px;top:598px;width:350px;color:var(--white)}
  .services__title{font-size:21px;font-weight:600;letter-spacing:.3px;display:inline-block;padding-bottom:6px;border-bottom:2px solid var(--white)}
  .services__list{list-style:none;margin-top:12px}
  .services__item{display:flex;align-items:center;gap:18px;font-size:17px;font-weight:600;height:40px}
  .services__icon{width:26px;height:26px;flex:none}
  .quote-mark{left:56px;top:478px;font-size:200px;font-weight:800;color:var(--quote-grey);line-height:1}
  .headline{left:60px;top:620px;width:370px;color:var(--gold);font-size:34px;font-weight:800;line-height:1.12}
  .projects{left:60px;top:786px;width:345px;color:var(--white);font-size:13px;line-height:1.4}
  .brand{left:110px;top:1000px;display:flex;align-items:center;gap:12px}
  .brand__square{width:30px;height:30px;background:var(--crimson)}
  .brand__name{font-size:34px;font-weight:700;color:var(--ink)}
  .address{left:70px;top:1058px;color:var(--muted);font-size:15px}
  .contact{left:470px;top:912px;color:var(--ink)}
  .contact__title{font-size:26px;font-weight:800;letter-spacing:.5px;line-height:1.2}
  .contact__sub{font-size:12px;font-weight:500;letter-spacing:.6px;text-transform:uppercase;padding-bottom:8px;border-bottom:1px solid #bbb;display:inline-block}
  .contact__row{display:flex;align-items:center;gap:8px;font-size:16px;margin-top:4px}
  .contact__row--phone{color:var(--crimson);font-size:28px;font-weight:600;margin-top:8px}
  .contact__icon{width:18px;height:18px;flex:none}
</style>
</head>
<body>
<main class="flyer">
  <svg class="flyer-shapes" viewBox="0 0 800 1130">
    <defs>
      <linearGradient id="stadium-tones" x1="0" y1="0" x2="0" y2="1">
        <stop offset="0" stop-color="#8f9aa6"/>
        <stop offset=".3" stop-color="#6d7075"/>
        <stop offset=".55" stop-color="#4f7a3a"/>
        <stop offset=".75" stop-color="#9a5a45"/>
        <stop offset="1" stop-color="#4a3d3a"/>
      </linearGradient>
    </defs>
    <rect role="img" aria-label="Photograph of a packed athletics stadium with track and field, seen from the stands" x="0" y="0" width="800" height="600" fill="url(#stadium-tones)"/>
    <path d="M0 380 C 200 640 520 520 800 240 L800 1130 L0 1130 Z" fill="var(--crimson)"/>
    <path d="M0 405 C 220 590 520 470 800 260 L800 1130 L0 1130 Z" fill="var(--charcoal)"/>
    <circle cx="190" cy="200" r="235" fill="var(--sky-blue)"/>
    <path d="M0 1130 L0 960 C 250 900 520 870 800 870 L800 1130 Z" fill="var(--sky-blue)"/>
    <path d="M0 1130 L0 982 C 260 922 530 893 800 895 L800 1130 Z" fill="var(--white)"/>
  </svg>

  <section class="event-badge abs">
    <p class="event-badge__lead">Broadcasting Northgate Athletics Games 2017 was a race that required skill, practice &amp; finest teamwork.</p>
    <p class="event-badge__claim">We Proved Ourselves yet again.</p>
    <p class="event-badge__note">*as cabling partners for broadcast television</p>
  </section>

  <p class="about abs">Velto Wire provide cabling services for Broadcast Television and Audio Visual systems. With over 15 years experience working in these industries we can help with every aspect of design, project managment, installation and maintenance.</p>

  <section class="services abs">
    <h2 class="services__title">OUR SERVICES</h2>
    <ul class="services__list">
      <li class="services__item">
        <svg class="services__icon" viewBox="0 0 26 26" fill="none" stroke="#fff" stroke-width="1.6"><path d="M6 9a9 9 0 0 1 14 0M9 12a5 5 0 0 1 8 0"/><path d="M13 13 9 24M13 13l4 11M10.5 20h5"/></svg>
        Broadcast/ AV System Design</li>
      <li class="services__item">
        <svg class="services__icon" viewBox="0 0 26 26" fill="#fff"><circle cx="13" cy="11" r="7"/><circle cx="13" cy="11" r="2.6" fill="var(--charcoal)"/><rect x="11" y="1" width="4" height="4"/><rect x="11" y="17" width="4" height="4"/><rect x="3" y="9" width="4" height="4"/><rect x="19" y="9" width="4" height="4"/><rect x="3" y="23" width="20" height="2"/></svg>
        On-site Installation</li>
      <li class="services__item">
        <svg class="services__icon" viewBox="0 0 26 26" fill="#fff"><rect x="2" y="3" width="22" height="5"/><rect x="2" y="10.5" width="22" height="5"/><rect x="2" y="18" width="22" height="5"/></svg>
        Rack Building</li>
      <li class="services__item">
        <svg class="services__icon" viewBox="0 0 26 26" fill="none" stroke="#fff" stroke-width="1.5"><rect x="4" y="4" width="16" height="18"/><path d="M4 10l6-6M4 16 16 4M4 22 20 6M10 22l10-10"/></svg>
        Pre-fabricated Cable Looms</li>
      <li class="services__item">
        <svg class="services__icon" viewBox="0 0 26 26" fill="none" stroke="#fff" stroke-width="1.5"><path d="M13 25V12M13 12 6 3M13 12l7-9M13 12V2M13 12 4 8M13 12l9-4"/></svg>
        Fibre optic installation</li>
    </ul>
  </section>

  <div class="quote-mark abs" aria-hidden="true">“</div>
  <h1 class="headline abs">Making the connections that digital innovation demands</h1>
  <p class="projects abs">Our projects range from fibre optic cabling at major sports events to installing and commisioning bespoke control systems on some of the worlds largest super yachts. The company based in London has executed projects successfully across Europe.</p>

  <div class="brand abs"><span class="brand__square"></span><span class="brand__name">Velto Wire</span></div>
  <p class="address abs">48 Foundry Lane, London, UK E3 2PX</p>

  <section class="contact abs">
    <h2 class="contact__title">GET A QUOTE</h2>
    <p class="contact__sub">Feel free to contact us.</p>
    <p class="contact__row contact__row--phone">
      <svg class="contact__icon" viewBox="0 0 24 24" fill="var(--crimson)"><path d="M6.6 10.8a15 15 0 0 0 6.6 6.6l2.2-2.2c.3-.3.7-.4 1-.2 1.1.4 2.3.6 3.6.6.6 0 1 .4 1 1V20c0 .6-.4 1-1 1A17 17 0 0 1 3 4c0-.6.4-1 1-1h3.5c.6 0 1 .4 1 1 0 1.3.2 2.5.6 3.6.1.3 0 .7-.2 1z"/></svg>
      01632 960 482</p>
    <p class="contact__row">
      <svg class="contact__icon" viewBox="0 0 24 24" fill="var(--ink)"><path d="M2 5h20v14H2z"/><path d="M2 5l10 8 10-8" fill="none" stroke="#fff" stroke-width="1.8"/></svg>
      info@velto-wire.example</p>
    <p class="contact__row">
      <svg class="contact__icon" viewBox="0 0 24 24" fill="var(--ink)"><path d="M12 3 2 12h3v9h5v-6h4v6h5v-9h3z"/></svg>
      www.velto-wire.example</p>
  </section>
</main>
</body>
</html>
```